Medical Staffing agency

I need a logo design that can stand along and become a brand. I'm not too particular of the design. Want something catchy and hopefully related to the Health field. Not important though. An example of what I'm looking for is the Stride Forge Logo, or the Vantora Logo. Something that can become a brand without having to say the brand name. A bit about my company, I hire medical staff, and contract with other companies to provide anywhere from short term to long term employees. But that is expanding to more than just that.

Industry/Entity Type

Medical

Contact Information for Business Card

Westmere Rehab Services
Dalen Whitcombe, CEO
742 Brookhollow Ave
Suite 48
Clovis, CA 95718

```html
<!DOCTYPE html>
<html lang="en">
<head>
<meta charset="utf-8">
<title>Westmere Rehab Services – Business Cards</title>
<link rel="stylesheet" href="https://fonts.googleapis.com/css2?family=Exo+2:wght@400;600;700&display=swap">
<style>
  :root {
    --backdrop: #cfcfcf;
    --card: #ffffff;
    --maroon: #7d2a3c;
    --maroon-dark: #6a2232;
    --ink: #1d1d1d;
    --muted: #4a4a4a;
    --frame: #151515;
    --accent-dark: #1a1a1a;
  }
  * { box-sizing: border-box; margin: 0; padding: 0; }
  html, body { width: 1200px; height: 894px; overflow: hidden; }
  body {
    background: var(--backdrop);
    font-family: "Exo 2", sans-serif;
    position: relative;
  }
  .card {
    position: absolute;
    width: 640px;
    height: 366px;
    background: var(--card);
    overflow: hidden;
  }
  .card-frame {
    position: absolute;
    inset: 22px;
    border: 3px solid var(--frame);
  }
  .band {
    position: absolute;
    left: 0; right: 0;
    background: linear-gradient(90deg, var(--maroon-dark), var(--maroon));
  }
  .brand {
    display: flex;
    align-items: center;
    gap: 12px;
    color: var(--maroon);
    font-weight: 700;
    line-height: 1.05;
  }
  .brand-mark {
    border-radius: 50%;
    background: var(--maroon);
    flex: none;
  }

  /* Logo side */
  .card-logo { left: 500px; top: 64px; }
  .card-logo .brand {
    position: absolute;
    top: 98px; left: 0; right: 0;
    justify-content: center;
    font-size: 30px;
  }
  .card-logo .brand-mark { width: 62px; height: 62px; }
  .card-logo .band {
    top: 232px; height: 56px;
    display: flex; align-items: center; justify-content: center;
  }
  .web-address {
    color: #fff;
    font-size: 24px;
    letter-spacing: 1px;
  }

  /* Contact side */
  .card-contact { left: 60px; top: 470px; }
  .card-contact .brand {
    position: absolute;
    top: 46px; left: 56px;
    font-size: 20px;
  }
  .card-contact .brand-mark { width: 42px; height: 42px; }
  .contact-list {
    position: absolute;
    list-style: none;
    display: flex; flex-direction: column; gap: 12px;
    font-size: 15px;
    color: var(--muted);
  }
  .contact-list li { display: flex; align-items: center; gap: 10px; line-height: 1.25; }
  .contact-list svg { width: 22px; height: 22px; flex: none; }
  .contact-primary { top: 118px; left: 56px; }
  .contact-secondary { top: 192px; left: 352px; }
  .person {
    position: absolute;
    top: 120px; left: 352px;
  }
  .person-name { font-size: 22px; font-weight: 600; color: var(--ink); }
  .person-role { font-size: 15px; color: var(--muted); margin-top: 2px; }
  .card-contact .band { top: 296px; height: 40px; }
  .band-accent {
    position: absolute;
    left: 0; top: 296px;
    width: 46px; height: 40px;
    background: var(--accent-dark);
  }
</style>
</head>
<body>

<svg width="0" height="0" style="position:absolute" aria-hidden="true">
  <defs>
    <symbol id="icon-phone" viewBox="0 0 22 22">
      <rect width="22" height="22" rx="4" fill="#7d2a3c"/>
      <path d="M7 5.5c.6-.4 1.3-.2 1.6.4l1 1.8c.3.5.1 1.1-.3 1.4l-.7.5c.5 1.4 1.5 2.5 2.9 3.1l.5-.7c.3-.4.9-.6 1.4-.3l1.8 1c.6.3.8 1 .4 1.6l-.6.9c-.5.7-1.5 1-2.3.7C9.6 14.8 7.3 12.4 6.2 9.1c-.3-.8 0-1.8.7-2.3z" fill="#fff"/>
    </symbol>
    <symbol id="icon-mail" viewBox="0 0 22 22">
      <rect width="22" height="22" rx="4" fill="#7d2a3c"/>
      <rect x="5" y="7" width="12" height="8.5" rx="1" fill="#fff"/>
      <path d="M5.5 7.6 11 11.6l5.5-4" fill="none" stroke="#7d2a3c" stroke-width="1.2"/>
    </symbol>
    <symbol id="icon-pin" viewBox="0 0 22 22">
      <rect width="22" height="22" rx="4" fill="#7d2a3c"/>
      <path d="M11 4.5a4.3 4.3 0 0 0-4.3 4.3c0 3.2 4.3 8.7 4.3 8.7s4.3-5.5 4.3-8.7A4.3 4.3 0 0 0 11 4.5z" fill="#fff"/>
      <circle cx="11" cy="8.8" r="1.6" fill="#7d2a3c"/>
    </symbol>
    <symbol id="icon-web" viewBox="0 0 22 22">
      <rect width="22" height="22" rx="4" fill="#7d2a3c"/>
      <g fill="none" stroke="#fff" stroke-width="1.2">
        <circle cx="11" cy="11" r="5.5"/>
        <ellipse cx="11" cy="11" rx="2.3" ry="5.5"/>
        <path d="M5.5 11h11M6.3 8.2h9.4M6.3 13.8h9.4"/>
      </g>
    </symbol>
  </defs>
</svg>

<section class="card card-logo" aria-label="Business card, logo side">
  <div class="card-frame"></div>
  <div class="brand">
    <span class="brand-mark"></span>
    <span class="brand-name">Westmere Rehab<br>Services</span>
  </div>
  <div class="band">
    <span class="web-address">www.westmererehab.com</span>
  </div>
</section>

<section class="card card-contact" aria-label="Business card, contact side">
  <div class="card-frame"></div>
  <div class="brand">
    <span class="brand-mark"></span>
    <span class="brand-name">Westmere Rehab<br>Services</span>
  </div>

  <ul class="contact-list contact-primary">
    <li><svg><use href="#icon-phone"/></svg>014 582 6390</li>
    <li><svg><use href="#icon-mail"/></svg>dalen@westmererehab.com</li>
  </ul>

  <div class="person">
    <p class="person-name">Dalen Whitcombe</p>
    <p class="person-role">CEO</p>
  </div>

  <ul class="contact-list contact-secondary">
    <li><svg><use href="#icon-pin"/></svg><span>742 Brookhollow Ave, Suite 48<br>Clovis, CA 95718</span></li>
    <li><svg><use href="#icon-web"/></svg>www.westmererehab.com</li>
  </ul>

  <div class="band"></div>
  <div class="band-accent"></div>
</section>

</body>
</html>
```